Branvique needs a business Card Design

We are looking for a business card Design for our new Managed Service Provider Company, Branvique. Branvique encompasses everything IT for the average medium sized business. Our primary services are help desk support, cyber-security (malware and ransomware protection), and Disaster Recovery systems. We would like the design to have a very clean and professional look, with a very minimalist feel.

Target Market(s)

Medium to large sized businesses

Industry/Entity Type

It Service

Contact Information for Business Card

Name GoesHere
name@branvique.com
O: 555-382-6047
C: 555-731-5820

Font styles to use
Other font styles liked:
• Poppins Font Only Please

Colors

Designer to choose only greyscale colors for use in the design.

Requirements
Must have
• Logo included
Nice to have
• Cutting Edge, innovative, minimalistic, elegant

```html
<!DOCTYPE html>
<html lang="en">
<head>
<meta charset="utf-8">
<title>Branvique Business Card</title>
<link rel="stylesheet" href="https://fonts.googleapis.com/css2?family=Poppins:wght@400&display=swap">
<style>
  :root {
    --backdrop: #e6e5e3;
    --card-light: #ffffff;
    --card-dark: #2e2e2e;
    --ink-dark: #1f1f1f;
    --ink-grey: #4a4a4a;
    --ink-white: #ffffff;
    --card-shadow: rgba(0, 0, 0, 0.28);
  }
  * { box-sizing: border-box; margin: 0; padding: 0; }
  html, body {
    width: 900px;
    height: 1200px;
    overflow: hidden;
  }
  body {
    position: relative;
    background: var(--backdrop);
    font-family: "Poppins", sans-serif;
  }
  .card {
    position: absolute;
    left: 86px;
    width: 735px;
    height: 430px;
    box-shadow: 0 6px 14px var(--card-shadow);
  }
  .card--front { top: 137px; background: var(--card-light); }
  .card--back  { top: 633px; background: var(--card-dark); }

  .brand-name {
    position: absolute;
    font-weight: 400;
    white-space: nowrap;
    line-height: 1;
    text-align: center;
  }
  .card--front .brand-name {
    left: 0;
    width: 394px;
    top: 250px;
    font-size: 36px;
    color: var(--ink-dark);
  }
  .card--back .brand-name {
    left: 0;
    width: 100%;
    top: 262px;
    font-size: 42px;
    color: var(--ink-white);
  }

  .divider {
    position: absolute;
    left: 400px;
    top: 120px;
    width: 4px;
    height: 194px;
  }

  .contact-block {
    position: absolute;
    left: 433px;
    top: 122px;
  }
  .holder-name {
    font-size: 28px;
    font-weight: 400;
    color: var(--ink-dark);
    line-height: 1.2;
  }
  .holder-title {
    font-size: 16.5px;
    font-weight: 400;
    color: var(--ink-grey);
    line-height: 1.3;
    margin-bottom: 26px;
  }
  .contact-list { list-style: none; }
  .contact-item {
    display: flex;
    align-items: center;
    height: 26px;
    font-size: 17.5px;
    font-weight: 400;
    color: var(--ink-grey);
  }
  .contact-icon {
    width: 14px;
    height: 14px;
    margin-right: 10px;
    fill: var(--ink-dark);
    flex: none;
  }
</style>
</head>
<body>
  <section class="card card--front" aria-label="Business card front">
    <div class="brand-name">Branvique</div>

    <svg class="divider" viewBox="0 0 4 194" aria-hidden="true">
      <path d="M2 0 L3.2 97 L2 194 L0.8 97 Z" fill="#1f1f1f"/>
    </svg>

    <div class="contact-block">
      <h1 class="holder-name">Daniel Carver</h1>
      <p class="holder-title">Founder &amp; CEO</p>
      <ul class="contact-list">
        <li class="contact-item">
          <svg class="contact-icon" viewBox="0 0 16 16" aria-hidden="true">
            <path d="M3.6 1.2l2.2 2.6-1.2 1.8c.9 2 2.6 3.7 4.6 4.6l1.8-1.2 2.6 2.2-1.4 2.6C6.6 13.6 2.4 9.4 1 3.6z"/>
          </svg>555-382-6047
        </li>
        <li class="contact-item">
          <svg class="contact-icon" viewBox="0 0 16 16" aria-hidden="true">
            <path d="M4.5 0.5h7a1 1 0 0 1 1 1v13a1 1 0 0 1-1 1h-7a1 1 0 0 1-1-1v-13a1 1 0 0 1 1-1zm.6 2v10h5.8v-10zm2.9 10.7a.8.8 0 1 0 0 1.6.8.8 0 0 0 0-1.6z"/>
          </svg>555-731-5820
        </li>
        <li class="contact-item">
          <svg class="contact-icon" viewBox="0 0 16 16" aria-hidden="true">
            <path d="M1 3.5h14v1.2L8 9 1 4.7z M1 6.2l7 4.3 7-4.3V12.5H1z"/>
          </svg>name@branvique.com
        </li>
        <li class="contact-item">
          <svg class="contact-icon" viewBox="0 0 16 16" aria-hidden="true">
            <path d="M8 1a7 7 0 1 0 0 14A7 7 0 0 0 8 1zm5.4 6.3h-2.5a11 11 0 0 0-.8-4.1 5.6 5.6 0 0 1 3.3 4.1zM8 2.4c.7.9 1.3 2.6 1.5 4.9h-3C6.7 5 7.3 3.3 8 2.4zM5.9 3.2a11 11 0 0 0-.8 4.1H2.6a5.6 5.6 0 0 1 3.3-4.1zM2.6 8.7h2.5a11 11 0 0 0 .8 4.1 5.6 5.6 0 0 1-3.3-4.1zM8 13.6c-.7-.9-1.3-2.6-1.5-4.9h3c-.2 2.3-.8 4-1.5 4.9zm2.1-.8a11 11 0 0 0 .8-4.1h2.5a5.6 5.6 0 0 1-3.3 4.1z"/>
          </svg>www.branvique.com
        </li>
      </ul>
    </div>
  </section>

  <section class="card card--back" aria-label="Business card back">
    <div class="brand-name">Branvique</div>
  </section>
</body>
</html>
```